ONE PAGE WEB DESIGN NEEDED for Finance Company

We need a web design (ONE PAGE DESIGN ONLY) for a new finance website called Corvella Lending. Corvella Lending helps customers get the right loan, whether its a home loan, investment loan, business loan etc.

You are required to come up with just the homepage design. Professionalism and quality is the key factors in the successful design.

Here are a few design questions to help you out:

-
What information should be used on the page?
Ive provided a document which outlines all the information needed to put on homepage (attached to the brief - called corvella_page_info). Also see the Must Have section below on this brief.

-
What links should appear in the navigation/footer?:
The navigation should provide links to the following pages (NOTE: services link has subcategories):
1 Homepage
2 Services
- Home loans
- Investment loans
- Refinancing loans
- Business loans
3 About Us
4 FAQ
5 Contact Us

-
What colors should be used in the design?
Our company colors - Cyan: #2EADE3, Blue: #004B70, White. Feel free to submit designs with slight variations if you feel it improves the design.

-
What should the layout of the page be?
This is up to you to come up with - we are open to different layouts for the page design (as long as they capture the information effectively and making it easy to understand).

Target Market(s)

Potential Home owners, Families and Business Owners

Industry/Entity Type

Business

Requirements
Must have
• - Must contain our logo (attached as PNG and Illustrator file)
- Winning designer must supply a Photoshop file (PSD) that will allow us.
Nice to have
• - Should include photos/images of families, professional groups, tradespeople etc (you can use stock photos from PixelVaultImages and I will purchase them once you are selected as the winning design)
- Link to a loan calculator somewhere on front page with a button 'Find out how much you could borrow' (or maybe even try adding a loan calculator to the homepage if you think this would look good)
- Page should have a main headline "Finding the right loan for you" or "Corvella Lending finds the right loan for our customers."
- Must include Accreditation logos somewhere on the homepage (will try and supply these soon)
Should not have
• - Poor quality designs will not be considered
- Do not use clipart

```html
<!DOCTYPE html>
<html lang="en">
<head>
<meta charset="utf-8">
<title>Corvella Lending</title>
<link rel="stylesheet" href="https://fonts.googleapis.com/css2?family=Open+Sans:ital,wght@0,400;0,600;0,700&family=PT+Serif:ital,wght@1,400&display=swap">
<style>
:root{
  --cyan:#2eade3;
  --cyan-light:#4fc6f0;
  --cyan-deep:#1f93d3;
  --navy:#0b4a6e;
  --ink:#333;
  --muted:#8a8a8a;
  --band:#f3f3f3;
  --line:#dcdcdc;
  --orange:#f7a21b;
  --orange-light:#fbbf3a;
  --green:#2f9e2f;
  --footer:#e8e8e8;
  --white:#fff;
}
*{box-sizing:border-box;margin:0;padding:0}
html,body{width:1034px;height:1200px;overflow:hidden}
body{position:relative;background:#fbfbfb;font-family:"Open Sans",Arial,sans-serif;color:var(--ink)}
.abs{position:absolute}
a{color:inherit;text-decoration:none}

/* header */
.site-header{left:0;top:0;width:1034px;height:109px;background:linear-gradient(#f1f1f1,#fafafa);border-bottom:1px solid var(--line)}
.brand{left:113px;top:20px;display:flex;align-items:flex-end;gap:8px}
.brand-mark{width:34px;height:34px;border-radius:50%;border:4px solid var(--cyan);margin-bottom:6px}
.brand-name{font-size:21px;font-weight:600;color:var(--navy);letter-spacing:-.3px;line-height:1.6}
.account-links{right:112px;top:24px;font-size:11px;color:#777}
.main-nav{left:403px;top:59px;display:flex}
.main-nav a{font-size:13px;color:var(--navy);font-weight:600;height:25px;line-height:25px;padding:0 8px;margin-right:8px;white-space:nowrap}
.main-nav a.is-active{background:var(--cyan);color:var(--white);border-radius:2px}
.header-phone{right:113px;top:58px;display:flex;align-items:center;gap:7px;font-size:17px;font-weight:700;color:var(--navy);border-left:3px double var(--navy);padding-left:10px;height:24px;white-space:nowrap;letter-spacing:-.2px}

/* hero */
.hero-photo{left:113px;top:110px;width:411px;height:309px;background:linear-gradient(135deg,#eef3f7,#d9dfe4 55%,#b7c0c8)}
.slider-dots{left:143px;top:401px;display:flex;gap:6px}
.slider-dots span{width:7px;height:7px;border-radius:50%;background:var(--white)}
.slider-dots span.on{background:var(--cyan)}
.hero-panel{left:524px;top:110px;width:397px;height:309px;background:linear-gradient(var(--cyan-light),var(--cyan-deep));color:var(--white);padding:36px 27px}
.hero-notch{left:503px;top:245px}
.hero-title{font-size:23px;font-weight:600;line-height:27px;letter-spacing:-.3px}
.hero-text{font-size:12px;line-height:16px;margin-top:4px;font-weight:600}
.btn-orange{display:flex;align-items:center;background:linear-gradient(var(--orange-light),var(--orange));color:var(--white);border-radius:2px;box-shadow:0 1px 2px rgba(0,0,0,.25);white-space:nowrap;overflow:hidden}
.btn-orange .bag{width:36px;flex:none;display:flex;justify-content:center;border-right:1px solid rgba(255,255,255,.5);height:70%;align-items:center}
.btn-orange .label{padding-left:11px;font-size:18px;letter-spacing:-.3px}
.hero-cta{margin-top:18px;width:234px;height:42px}
.loan-types{margin-top:14px;display:grid;grid-template-columns:154px 150px;row-gap:6px;font-size:12.5px;list-style:none}
.loan-types li{display:flex;align-items:center;gap:6px;white-space:nowrap}

/* accreditation band */
.accreditations{left:0;top:419px;width:1034px;height:76px;background:var(--band);border-top:1px solid var(--line);border-bottom:1px solid var(--line)}
.badge{position:absolute;top:24px;width:70px;height:26px;border-radius:3px;background:#cfcfcf}

/* welcome */
.welcome{left:116px;top:538px;width:540px}
.welcome h1{font-size:20px;font-weight:400;color:var(--navy)}
.welcome .lead{font-family:"PT Serif",Georgia,serif;font-style:italic;font-size:14.5px;line-height:18px;color:#222;margin-top:6px}
.welcome .body{font-size:11px;line-height:16.3px;color:var(--muted);margin-top:12px}

.help-box{left:684px;top:537px;width:237px;height:163px;background:linear-gradient(var(--cyan),var(--cyan-deep));border-radius:2px;color:var(--white);padding:14px 16px;overflow:hidden}
.help-box h2{font-size:14px;font-weight:700;display:flex;align-items:center;gap:6px;white-space:nowrap}
.help-box p{font-size:10.5px;line-height:13px;margin-top:6px}
.signup-form{display:flex;margin-top:10px;margin-left:4px}
.signup-form .field{width:169px;height:29px;background:var(--white);border:1px solid #ccc;font-size:11px;color:#aaa;line-height:27px;padding-left:8px}
.signup-form .go{width:32px;height:29px;background:var(--green);font-weight:700;font-size:13px;text-align:center;line-height:29px}
.call-now{display:flex;align-items:center;gap:8px;margin-top:10px;margin-left:4px;white-space:nowrap}
.call-now small{font-size:10px;font-weight:700;line-height:10px;border-right:1px solid #fff;padding-right:6px}
.call-now strong{font-size:24px;font-weight:700;letter-spacing:-.3px;line-height:28px}

/* cta bar */
.cta-bar{left:113px;top:739px;width:808px;height:63px;background:#f1f1f1;border:1px solid var(--line)}
.cta-icon{left:12px;top:17px}
.cta-bar h2{position:absolute;left:46px;top:10px;font-size:19px;font-weight:400;color:#333;white-space:nowrap}
.cta-bar p{position:absolute;left:46px;top:35px;font-size:12px;color:var(--muted);white-space:nowrap}
.cta-btn{position:absolute;left:541px;top:10px;width:251px;height:42px}

/* calculator */
.calculator-card{left:113px;top:843px;width:369px;height:133px;background:linear-gradient(#f6f6f6,#e9e9e9);border:1px solid var(--line);box-shadow:0 2px 3px rgba(0,0,0,.15)}
.calc-art{position:absolute;left:15px;top:30px;width:74px;height:82px;border-radius:6px;background:linear-gradient(#3c3c3c,#1e1e1e)}
.calculator-card h3{position:absolute;left:103px;top:17px;font-size:13px;font-weight:400;color:#333}
.calculator-card p{position:absolute;left:103px;top:35px;width:245px;font-size:10.5px;line-height:13px;color:var(--muted)}
.btn-blue{position:absolute;left:104px;top:86px;width:230px;height:28px;background:linear-gradient(var(--cyan-light),var(--cyan-deep));color:var(--white);font-size:12.5px;line-height:28px;text-align:center;border-radius:2px;white-space:nowrap;letter-spacing:-.2px}

/* testimonial */
.testimonial-title{left:537px;top:850px;display:flex;align-items:center;gap:8px;font-size:13px;color:#333}
.quote-box{left:538px;top:872px;width:377px;height:79px;background:var(--white);border:1px solid var(--line);padding:12px 14px;font-size:10.5px;line-height:14.5px;color:var(--navy)}
.quote-box cite{position:absolute;right:14px;top:55px;font-style:normal}
.quote-tail{left:852px;top:950px}
.read-more{left:789px;top:959px;font-size:11px;font-weight:700;color:var(--cyan)}

/* footer */
.site-footer{left:0;top:1024px;width:1034px;height:176px;background:var(--footer)}
.footer-col{position:absolute;top:28px}
.footer-col h4{font-size:13px;font-weight:400;color:var(--navy);margin-bottom:6px}
.footer-col li{list-style:none;font-size:10.5px;line-height:16.5px;color:#555;display:flex;align-items:center;gap:6px;white-space:nowrap}
.social{display:flex;gap:8px;margin:6px 0 0 16px}
.social span{width:13px;height:13px;border-radius:50%}
.footer-ring{left:806px;top:24px;width:94px;height:94px;border-radius:50%;border:10px solid #d3d3d3}
.footer-rule{position:absolute;left:113px;top:146px;width:808px;border-top:1px solid #d6d6d6}
.copyright{position:absolute;left:113px;top:157px;font-size:9px;color:#555}
</style>
</head>
<body>

<header class="site-header abs">
  <div class="brand abs"><span class="brand-mark"></span><span class="brand-name">corvellalending</span></div>
  <div class="account-links abs">Sign up &nbsp;|&nbsp; Member Login</div>
  <nav class="main-nav abs">
    <a class="is-active" href="#">Home</a><a href="#">Services</a><a href="#">About Us</a><a href="#">FAQ</a><a href="#">Contact Us</a>
  </nav>
  <div class="header-phone abs">
    <svg width="20" height="16" viewBox="0 0 20 16"><path d="M2 5c0-3 16-3 16 0v2h-4V5H6v2H2z" fill="#0b4a6e"/><rect x="4" y="8" width="12" height="7" rx="1" fill="#0b4a6e"/><circle cx="10" cy="11.5" r="2" fill="#fff"/></svg>
    1800 555 010
  </div>
</header>

<div class="hero-photo abs" role="img" aria-label="Photo of three smiling colleagues working together at a desk"></div>
<div class="slider-dots abs"><span></span><span class="on"></span><span></span><span></span></div>
<section class="hero-panel abs">
  <h2 class="hero-title">Corvella Lending finds the right loan for our customers</h2>
  <p class="hero-text">Nemo enim ipsam voluptatem quia voluptas sit aspernatur aut odit aut fugit, sed quia consequuntur magni dolores eos qui ratione voluptatem...</p>
  <a class="btn-orange hero-cta" href="#">
    <span class="bag"><svg width="16" height="20" viewBox="0 0 16 20"><path d="M5 1h6l-2 4h2c4 3 5 7 5 10 0 3-3 4-8 4s-8-1-8-4c0-3 1-7 5-10h2z" fill="#fff"/><text x="8" y="16" font-size="8" text-anchor="middle" fill="#f7a21b" font-family="Arial,sans-serif" font-weight="700">$</text></svg></span>
    <span class="label">Find your Loan Now</span>
  </a>
  <ul class="loan-types">
    <li><svg width="12" height="10"><path d="M1 5l3 3 7-7" stroke="#fff" stroke-width="2.4" fill="none"/></svg>Home loans</li>
    <li><svg width="12" height="10"><path d="M1 5l3 3 7-7" stroke="#fff" stroke-width="2.4" fill="none"/></svg>Refinancing loans</li>
    <li><svg width="12" height="10"><path d="M1 5l3 3 7-7" stroke="#fff" stroke-width="2.4" fill="none"/></svg>Investment loans</li>
    <li><svg width="12" height="10"><path d="M1 5l3 3 7-7" stroke="#fff" stroke-width="2.4" fill="none"/></svg>Business loans</li>
  </ul>
</section>
<svg class="hero-notch abs" width="22" height="34" viewBox="0 0 22 34"><path d="M22 0v34L0 17z" fill="#31b1e6"/><path d="M11 19c1-4 4-5 7-5v-2l3 3-3 3v-2c-3 0-5 1-7 3z" fill="#fff"/></svg>

<section class="accreditations abs" aria-label="Accreditations">
  <span class="badge" style="left:105px"></span>
  <span class="badge" style="left:228px"></span>
  <span class="badge" style="left:351px"></span>
  <span class="badge" style="left:474px"></span>
  <span class="badge" style="left:597px"></span>
  <span class="badge" style="left:721px"></span>
  <span class="badge" style="left:842px"></span>
</section>

<section class="welcome abs">
  <h1>Welcome to the corvellalending</h1>
  <p class="lead">Nemo enim ipsam voluptatem quia voluptas sit aspernatur aut odit aut fugit, sed quia consequuntur magni dolores eos qui ratione voluptatem sequi nesciunt.</p>
  <p class="body">Neque porro quisquam est, qui. dolorem ipsum quia dolor sit amet, consectetur, adipisci velit, sed quia non numquam eius modi tempora incidunt ut labore et dolore magnam aliquam quaerat voluptatem. Neque porro quisquam est, qui. dolorem ipsum quia dolor sit amet, consectetur, adipisci velit, sed quia non numquam eius modi tempora incidunt ut labore.</p>
</section>

<aside class="help-box abs">
  <h2><svg width="16" height="12" viewBox="0 0 16 12"><rect x=".5" y=".5" width="15" height="11" fill="none" stroke="#fff"/><path d="M1 1l7 6 7-6" stroke="#fff" fill="none"/></svg>GET HELP INSTANTLY</h2>
  <p>Neque porro quisquam est, qui. dolorem ipsum quia dolor sit amet.</p>
  <div class="signup-form"><span class="field">Email Address</span><span class="go">Go</span></div>
  <div class="call-now"><small>CALL<br>NOW</small><strong>1847 555 019</strong></div>
</aside>

<section class="cta-bar abs">
  <svg class="cta-icon abs" width="26" height="28" viewBox="0 0 26 28"><circle cx="10" cy="10" r="7.5" stroke="#333" stroke-width="2.5" fill="none"/><path d="M15 16l9 9" stroke="#333" stroke-width="4" stroke-linecap="round"/></svg>
  <h2>Find your perfect small business loan</h2>
  <p>Sign up now to get Started with your free account</p>
  <a class="btn-orange cta-btn" href="#">
    <span class="bag"><svg width="16" height="20" viewBox="0 0 16 20"><path d="M5 1h6l-2 4h2c4 3 5 7 5 10 0 3-3 4-8 4s-8-1-8-4c0-3 1-7 5-10h2z" fill="#fff"/><text x="8" y="16" font-size="8" text-anchor="middle" fill="#f7a21b" font-family="Arial,sans-serif" font-weight="700">$</text></svg></span>
    <span class="label">Find Your Perfect Loan</span>
  </a>
</section>

<section class="calculator-card abs">
  <div class="calc-art" role="img" aria-label="Calculator icon with a green tick"></div>
  <h3>Loan Calculator</h3>
  <p>Ridewell Academy understands there is no substitute for being on a bike. Ridewell offers a motor-cycle class in.</p>
  <a class="btn-blue" href="#">Find out how much you could borrow</a>
</section>

<div class="testimonial-title abs"><svg width="14" height="12" viewBox="0 0 14 12"><rect width="14" height="9" rx="2" fill="#555"/><path d="M3 9v3l3-3z" fill="#555"/><circle cx="4" cy="4.5" r="1" fill="#fff"/><circle cx="7" cy="4.5" r="1" fill="#fff"/><circle cx="10" cy="4.5" r="1" fill="#fff"/></svg>Our Happy Customers</div>
<blockquote class="quote-box abs">"All graduates are offered the opportunity to take their licensing test at our site. Ninety percent of Ridewell students go on to pass the exam!"<cite>[ &nbsp;Owen Marsh&nbsp; ]</cite></blockquote>
<svg class="quote-tail abs" width="20" height="20" viewBox="0 0 20 20"><path d="M0 0h16l-12 18z" fill="#fff"/><path d="M16 0L4 18 4 0" stroke="#dcdcdc" fill="none"/></svg>
<a class="read-more abs" href="#">Read More</a>

<footer class="site-footer abs">
  <div class="footer-col" style="left:114px"><h4>Navigate</h4><ul><li>How it Works</li><li>Success Stories</li><li>Loan Types</li><li>Article Library</li></ul></div>
  <div class="footer-col" style="left:239px"><h4>Services</h4><ul><li>Home Loan</li><li>Investment Loan</li><li>Refinancing</li><li>Business Loan</li></ul></div>
  <div class="footer-col" style="left:364px"><h4>Responsible</h4><ul><li>Responsible Lending</li><li>Financial Advise</li><li>Smart Choice</li></ul></div>
  <div class="footer-col" style="left:510px"><h4>About Us</h4><ul><li>FAQs</li><li>Testimonials</li><li>Our Blog</li></ul></div>
  <div class="footer-col" style="left:615px"><h4>Contact Us</h4><ul>
    <li><svg width="8" height="11"><rect x="1" y=".5" width="6" height="10" rx="1" fill="none" stroke="#666"/></svg>1847 555 019</li>
    <li><svg width="9" height="7"><rect x=".5" y=".5" width="8" height="6" fill="none" stroke="#666"/><path d="M.5 .5l4 3 4-3" stroke="#666" fill="none"/></svg>info@corvellalending.com</li></ul>
    <div class="social"><span style="background:#2eade3"></span><span style="background:#1f5fa8"></span><span style="background:#e8711c"></span></div>
  </div>
  <div class="footer-ring abs"></div>
  <div class="footer-rule"></div>
  <p class="copyright">© copyright 2012 corvellalending &nbsp;All rights reserved.</p>
</footer>

</body>
</html>
```